Web App Dashboard Design for Healthcare Company

We have developed a simple web application with 3 navigation menus. We like the current design (very much modeled after Tallyworks), but we want to explore UI options for the branding, header, menus, and footer that we may not have considered.

The attached screenshots show the layout and two menu "hover" views as they currently exist.

This web application is used by employees only.

Menu 1 - Module Menu:
Allows the user to switch easily between Account, Employee, and Care Management.

Menu 2 - Reports Menu
Allows user to view available reports within each Module.

Menu 3 - Admin Menu
Allows the user to easily create new content types within each module.

Use our branded colors and font.

Colors:
Logo Blue (dark): 00c0f3
Logo Blue (light): 44c8f5
Nav Blue: 0994d0
Green: 71b44b
Grayscale: (not specified)

Font:
Lato (Google Font)

Target Market(s)

Internal staff.

Industry/Entity Type

Healthcare

Number of Pages Required

3 page

Font styles to use
Sans Serif
Other font styles liked:
• Lato (Google Font)

Colors
0293ce
9bcb3c

Requirements
Must have
• It's really a one page design, but we want to see the two "hover" views for the Module Menu and the Admin Menu.
• It should also be very clear which "Report" page the user is on (the active menu link).
• Must use branded colors, font, and logo.
• Logo Blue (dark): 00c0f3
• Logo Blue (light): 44c8f5
• Nav Blue: 0994d0
• Green: 71b44b
• Grayscale: Designer may choose
Nice to have
• It would be nice to have simple uncluttered payouts.
Should not have
• The design should not have menu options exposed by default.

```html
<!DOCTYPE html>
<html lang="en">
<head>
<meta charset="utf-8">
<title>Carevio Dashboard</title>
<link href="https://fonts.googleapis.com/css2?family=Lato:wght@300;400;700&display=swap" rel="stylesheet">
<style>
:root{
  --nav:#1f2d3d; --nav-line:#2c3b4c; --nav-text:#e6ecf2; --nav-muted:#8a9bb0;
  --page:#eef1f5; --panel:#ffffff; --line:#e7eaee; --text:#333a42; --muted:#a4abb3;
  --cyan:#00c0f3; --lime:#8cc34a; --blue:#1f8fd9; --violet:#a35fe0;
  --done:#1a73c7; --ongoing:#f6c000; --review:#71b44b; --pending:#a35fe0; --removed:#e02424;
  --green:#71b44b; --navblue:#0994d0; --badge-yellow:#f6c000;
}
*{box-sizing:border-box;margin:0;padding:0}
html,body{width:1200px;height:923px;overflow:hidden}
body{font-family:'Lato',sans-serif;background:var(--page);color:var(--text);position:relative;font-size:9px}
.sidebar{position:absolute;left:0;top:0;width:126px;height:923px;background:var(--nav);color:var(--nav-text)}
.brand{display:flex;align-items:center;gap:6px;padding:12px 0 0 30px;height:44px;font-size:15px;font-weight:700;color:var(--cyan)}
.brand-dot{width:10px;height:10px;border-radius:50%;background:var(--cyan)}
.nav-label{font-size:8.5px;color:var(--nav-muted);padding:6px 12px 10px}
.nav-item{display:flex;align-items:center;height:25px;padding:0 10px 0 12px;font-size:8.5px;gap:9px;white-space:nowrap}
.nav-item.active{background:#19242f}
.nav-item svg{width:9px;height:9px;fill:var(--nav-text);flex:none}
.nav-item .label{flex:1}
.nav-badge{width:12px;height:12px;border-radius:50%;font-size:7px;display:flex;align-items:center;justify-content:center;color:#fff;flex:none}
.chev{font-size:9px;color:var(--nav-muted);margin-left:2px;width:5px}
.nav-rule{border-top:1px solid var(--nav-line);margin-top:10px}
.topbar{position:absolute;left:126px;top:0;width:1074px;height:36px;background:#fff;border-bottom:1px solid var(--line);display:flex;align-items:center;font-size:8.5px}
.topbar .menu-toggle{margin-left:18px;width:12px;height:9px;border-top:2px solid #555;border-bottom:2px solid #555;position:relative}
.topbar .menu-toggle::after{content:"";position:absolute;left:0;right:0;top:1.5px;border-top:2px solid #555}
.account{margin-left:30px;display:flex;align-items:center;gap:5px;white-space:nowrap}
.caret{width:0;height:0;border-left:3px solid transparent;border-right:3px solid transparent;border-top:4px solid #555;margin-left:4px}
.search-pill{margin-left:30px;width:117px;height:18px;border-radius:9px;background:#eef0f3;color:#b6bcc3;font-size:8px;display:flex;align-items:center;justify-content:space-between;padding:0 8px}
.top-right{margin-left:auto;display:flex;align-items:center;gap:22px;padding-right:20px}
.icon-wrap{position:relative;width:12px;height:12px}
.icon-wrap svg{width:12px;height:12px;fill:#666}
.dot-count{position:absolute;top:-6px;right:-6px;width:10px;height:10px;border-radius:50%;background:#e02424;color:#fff;font-size:6px;display:flex;align-items:center;justify-content:center}
.me{display:flex;align-items:center;gap:8px;white-space:nowrap}
.avatar{border-radius:50%;background:linear-gradient(135deg,#c9a58a,#5b4a42);flex:none}
.me .avatar{width:20px;height:20px}
.page-head{position:absolute;left:126px;top:36px;width:924px;height:49px;background:#fff;border-bottom:1px solid var(--line);padding:11px 17px}
.page-head h1{font-size:13px;font-weight:400}
.page-head p{font-size:7.5px;color:#c3c8cd;margin-top:2px}
.stat{position:absolute;top:103px;width:163px;height:68px;color:#fff;text-align:center;overflow:hidden}
.stat b{display:block;font-size:25px;font-weight:400;padding-top:13px;line-height:1}
.stat span{font-size:7px;opacity:.85}
.stat svg{position:absolute;left:0;bottom:0;width:163px;height:14px}
.panel{position:absolute;background:var(--panel)}
.panel-head{height:31px;border-bottom:1px solid var(--line);display:flex;align-items:center;padding:0 15px;font-size:11.5px}
.panel-head .right{margin-left:auto;display:flex;align-items:center;gap:14px;font-size:11.5px;color:#444}
.contents{left:144px;top:186px;width:891px;height:390px}
.toolbar{display:flex;padding:13px 16px;border-bottom:1px solid var(--line);height:52px;align-items:flex-start}
.field{height:23px;border:1px solid #e2e5e9;display:flex;align-items:center;padding:0 8px;font-size:8.5px}
.table{margin:0 15px;width:861px;border-collapse:collapse;font-size:8.5px;table-layout:fixed}
.table th{font-weight:700;text-align:left;height:34px;padding-top:14px;border-bottom:1px solid var(--line);font-size:8.5px}
.table td{height:42px;border-bottom:1px solid var(--line);white-space:nowrap}
.table tr.alt td{background:#f6f7f9}
.chk{width:12px;height:12px;border:1px solid #d6dadf;background:#fff;margin-left:12px}
.person{display:flex;align-items:center;gap:11px;font-weight:700}
.person .avatar{width:29px;height:29px}
.status{display:inline-block;width:47px;height:15px;line-height:15px;text-align:center;color:#fff;font-size:8px}
.act{display:flex;gap:4px;margin-left:71px}
.act span{width:17px;height:17px;border:1px solid #dde0e4;display:flex;align-items:center;justify-content:center}
.act svg{width:8px;height:8px;stroke:#888;fill:none;stroke-width:1.2}
.table-foot{display:flex;justify-content:space-between;align-items:center;padding:20px 15px;font-size:8px;color:var(--muted)}
.pager{display:flex;border:1px solid #e2e5e9}
.pager span{width:23px;height:22px;display:flex;align-items:center;justify-content:center;color:#444;border-left:1px solid #e2e5e9;font-size:8.5px}
.pager span:first-child{border-left:none}
.pager span.on{background:#f1f3f5}
.count{background:var(--green);color:#fff;font-size:8.5px;padding:2px 4px}
.count.blue{background:var(--blue)}
.list{padding:10px 15px}
.member{display:flex;align-items:center;gap:10px;height:49px}
.member .avatar{width:29px;height:29px;position:relative}
.member .avatar.on::after{content:"";position:absolute;right:-1px;top:0;width:5px;height:5px;border-radius:50%;background:#35d05a}
.member .nm{font-size:9px}
.member .role{font-size:8px;color:var(--muted)}
.task{display:flex;gap:18px;padding:0 15px}
.timeline{position:relative;width:14px}
.task-list{flex:1}
.task-item{border-bottom:1px solid var(--line);padding:14px 0 12px}
.task-item:last-child{border-bottom:none}
.task-item p{font-size:8.5px;white-space:nowrap}
.task-item .m{color:var(--muted)}
.task-item .time{color:var(--muted);font-size:8.5px;margin-top:8px;display:flex;align-items:center;gap:6px}
.clock{width:9px;height:9px;border:1px solid #b9bfc6;border-radius:50%}
.t-dot{position:absolute;left:0;width:14px;height:14px;border-radius:50%;color:#fff;font-size:8px;display:flex;align-items:center;justify-content:center;border:2px solid #f1f3f5}
.faces{display:flex;gap:9px;margin-top:9px}
.faces .avatar{width:31px;height:31px}
.notice{margin:12px 15px 0;height:21px;background:#eef7e6;color:#5f9a3a;font-size:8.5px;display:flex;align-items:center;justify-content:space-between;padding:0 9px}
.act-item{display:flex;gap:11px;padding:0 15px;height:51px;align-items:center;position:relative}
.act-item .avatar{width:29px;height:29px}
.act-item p{font-size:8.5px;line-height:1.3;white-space:nowrap}
.act-item .m{color:var(--muted)}
.aside{position:absolute;left:1050px;top:36px;width:150px;height:887px;background:#fff;border-left:1px solid var(--line)}
.aside .tab{height:49px;border-bottom:1px solid var(--line);position:relative}
.aside .tab::after{content:"";position:absolute;left:0;bottom:-1px;width:50px;border-bottom:2px solid #555}
.aside h3{font-size:8.5px;font-weight:700;padding:17px 16px 0}
.note-btn{position:absolute;left:16px;top:300px;width:118px;height:21px;background:var(--blue);color:#fff;font-size:8.5px;display:flex;align-items:center;justify-content:center}
.todo{position:absolute;left:0;top:340px;width:150px;border-top:1px solid var(--line);padding:17px 15px}
.todo h4{font-size:8.5px;font-weight:700}
.todo .sub{font-size:8px;color:#c0c5cb;margin-top:3px}
.todo-item{display:flex;align-items:center;gap:7px;height:30px;font-size:8.5px;white-space:nowrap}
.todo-item:first-of-type{margin-top:6px}
.box{width:8px;height:8px;border:1px solid #d9dde1;border-radius:1px}
.box.on{background:var(--blue);border-color:var(--blue);position:relative}
.box.on::after{content:"";position:absolute;left:2px;top:0;width:2px;height:4px;border:solid #fff;border-width:0 1px 1px 0;transform:rotate(45deg)}
.todo-add{display:flex;margin-top:14px}
.todo-add .in{width:85px;height:21px;border:1px solid #e2e5e9;font-size:8px;color:#bcc2c8;display:flex;align-items:center;padding-left:7px}
.todo-add .go{width:34px;height:21px;background:var(--blue);color:#fff;font-size:8.5px;font-weight:700;display:flex;align-items:center;justify-content:center}
</style>
</head>
<body>

<aside class="sidebar">
  <div class="brand"><span>Carevio</span><span class="brand-dot"></span></div>
  <div class="nav-label">Navigation</div>
  <div class="nav-item active"><svg viewBox="0 0 10 10"><path d="M5 1a4.5 4.5 0 0 0-4.5 4.5V8h9V5.5A4.5 4.5 0 0 0 5 1z"/></svg><span class="label">Reminders</span><span class="nav-badge" style="background:var(--green)">2</span><span class="chev">›</span></div>
  <div class="nav-item"><svg viewBox="0 0 10 10"><path d="M0 2h10v6H0z"/></svg><span class="label">Accounts</span><span class="chev"></span></div>
  <div class="nav-item"><svg viewBox="0 0 10 10"><path d="M1 2h8v7H1zM2 0h1v2H2zM7 0h1v2H7z"/></svg><span class="label">Patient Requests</span><span class="nav-badge" style="background:var(--navblue)">5</span><span class="chev"></span></div>
  <div class="nav-item"><svg viewBox="0 0 10 10"><path d="M2 0h4l2 2v8H2z"/></svg><span class="label">Reports</span><span class="nav-badge" style="background:var(--badge-yellow)">8</span><span class="chev">›</span></div>
  <div class="nav-item"><svg viewBox="0 0 10 10"><path d="M0 1h4v3H0zM5 1h5v3H5zM0 5h4v4H0zM5 5h5v4H5z"/></svg><span class="label">My Company</span><span class="chev">›</span></div>
  <div class="nav-rule"></div>
</aside>

<header class="topbar">
  <span class="menu-toggle"></span>
  <span class="account"><svg width="9" height="10" viewBox="0 0 10 10" fill="#555"><circle cx="5" cy="3" r="2.5"/><path d="M0 10a5 4 0 0 1 10 0z"/></svg>Account Management<span class="caret"></span></span>
  <span class="search-pill">Search projects...<svg width="8" height="8" viewBox="0 0 10 10" fill="none" stroke="#999" stroke-width="1.5"><circle cx="4" cy="4" r="3"/><path d="M6.5 6.5 9 9"/></svg></span>
  <div class="top-right">
    <span class="account" style="margin:0"><svg width="10" height="10" viewBox="0 0 10 10" fill="#999"><circle cx="5" cy="5" r="3.5"/><circle cx="5" cy="5" r="1.5" fill="#fff"/></svg>Settings<span class="caret"></span></span>
    <span class="icon-wrap"><svg viewBox="0 0 12 12"><path d="M1 2h10v9H1zM2 4h8v6H2z" fill-rule="evenodd"/></svg><span class="dot-count">5</span></span>
    <span class="icon-wrap" style="margin-left:18px"><svg viewBox="0 0 12 12"><path d="M6 1a3.5 3.5 0 0 0-3.5 3.5V8L1 9.5h10L9.5 8V4.5A3.5 3.5 0 0 0 6 1zM5 10.5h2a1 1 0 0 1-2 0z"/></svg><span class="dot-count">2</span></span>
    <span class="me" style="margin-left:18px">My Info<span class="caret"></span><span class="avatar" role="img" aria-label="User profile photo"></span></span>
  </div>
</header>

<section class="page-head"><h1>Dashboard</h1><p>Dashboard &amp; statistics</p></section>

<div class="stat" style="left:144px;background:var(--cyan)"><b>132</b><span>Contents Created</span><svg viewBox="0 0 163 14"><path d="M0 12 20 10 35 13 55 8 70 12 90 9 110 13 130 7 145 12 163 10" fill="none" stroke="rgba(255,255,255,.35)"/></svg></div>
<div class="stat" style="left:326px;background:var(--lime)"><b>18</b><span>Modules</span><svg viewBox="0 0 163 14"><path d="M0 12 20 9 35 13 55 10 70 6 90 12 110 9 130 13 145 8 163 11" fill="none" stroke="rgba(255,255,255,.35)"/></svg></div>
<div class="stat" style="left:508px;background:var(--blue)"><b>25</b><span>Reports</span><svg viewBox="0 0 163 14"><path d="M0 11 20 13 35 8 55 12 70 9 90 13 110 6 130 11 145 9 163 12" fill="none" stroke="rgba(255,255,255,.35)"/></svg></div>
<div class="stat" style="left:690px;background:var(--violet)"><b>3</b><span>In To Do list</span><svg viewBox="0 0 163 14"><path d="M0 13 20 7 35 12 55 9 70 13 90 8 110 12 130 9 145 13 163 9" fill="none" stroke="rgba(255,255,255,.35)"/></svg></div>

<section class="panel contents">
  <div class="panel-head" style="height:32px">Contents Table<span class="right">Add New Content<svg width="10" height="10" viewBox="0 0 10 10" fill="#888"><circle cx="5" cy="5" r="4"/><circle cx="5" cy="5" r="1.6" fill="#fff"/></svg></span></div>
  <div class="toolbar">
    <div class="field" style="width:142px;justify-content:space-between">Bulk Action<span class="caret"></span></div>
    <div class="field" style="width:58px;margin-left:7px;justify-content:center">Apply</div>
    <div class="field" style="width:119px;margin-left:auto">Search</div>
    <div class="field" style="width:23px;border-left:none;padding:0;justify-content:center">Go</div>
  </div>
  <table class="table">
    <colgroup><col style="width:40px"><col style="width:168px"><col style="width:280px"><col style="width:144px"><col style="width:96px"><col></colgroup>
    <tr><th></th><th>NAME</th><th>TASK</th><th>DATE</th><th style="text-align:center">STATUS</th><th style="padding-left:71px">ACTION</th></tr>
    <tr class="alt"><td><div class="chk"></div></td><td><div class="person"><span class="avatar" role="img" aria-label="Team member photo"></span>Shaunta Pollan</div></td><td>Sketch out new idea for promote Our webapp</td><td>Jul 25, 2015</td><td style="text-align:center"><span class="status" style="background:var(--done)">Done</span></td><td><div class="act"><span><svg viewBox="0 0 8 8"><path d="M1 7h5V3M2 5l4-4 1 1-4 4H2z"/></svg></span><span><svg viewBox="0 0 8 8"><path d="M1.5 2h5M2 2v5h4V2M3 1h2"/></svg></span></div></td></tr>
    <tr><td><div class="chk"></div></td><td><div class="person"><span class="avatar" role="img" aria-label="Team member photo"></span>Ronald Reck</div></td><td>Create Design based on promotional page for Pennly Pay</td><td>Jul 25, 2015</td><td style="text-align:center"><span class="status" style="background:var(--ongoing)">Ongoing</span></td><td><div class="act"><span><svg viewBox="0 0 8 8"><path d="M1 7h5V3M2 5l4-4 1 1-4 4H2z"/></svg></span><span><svg viewBox="0 0 8 8"><path d="M1.5 2h5M2 2v5h4V2M3 1h2"/></svg></span></div></td></tr>
    <tr class="alt"><td><div class="chk"></div></td><td><div class="person"><span class="avatar" role="img" aria-label="Team member photo"></span>Kristine Spindler</div></td><td>Design responsive template for Our webapp</td><td>Jul 25, 2015</td><td style="text-align:center"><span class="status" style="background:var(--review)">In Review</span></td><td><div class="act"><span><svg viewBox="0 0 8 8"><path d="M1 7h5V3M2 5l4-4 1 1-4 4H2z"/></svg></span><span><svg viewBox="0 0 8 8"><path d="M1.5 2h5M2 2v5h4V2M3 1h2"/></svg></span></div></td></tr>
    <tr><td><div class="chk"></div></td><td><div class="person"><span class="avatar" role="img" aria-label="Team member photo"></span>Randolph Seckman</div></td><td>Side bar enhancement for Merchant Panel</td><td>Jul 25, 2015</td><td style="text-align:center"><span class="status" style="background:var(--pending)">Pending</span></td><td><div class="act"><span><svg viewBox="0 0 8 8"><path d="M1 7h5V3M2 5l4-4 1 1-4 4H2z"/></svg></span><span><svg viewBox="0 0 8 8"><path d="M1.5 2h5M2 2v5h4V2M3 1h2"/></svg></span></div></td></tr>
    <tr class="alt"><td><div class="chk"></div></td><td><div class="person"><span class="avatar" role="img" aria-label="Team member photo"></span>Bailey Angell</div></td><td>Plan for team building activity QII</td><td>Jul 25, 2015</td><td style="text-align:center"><span class="status" style="background:var(--removed)">Removed</span></td><td><div class="act"><span><svg viewBox="0 0 8 8"><path d="M1 7h5V3M2 5l4-4 1 1-4 4H2z"/></svg></span><span><svg viewBox="0 0 8 8"><path d="M1.5 2h5M2 2v5h4V2M3 1h2"/></svg></span></div></td></tr>
  </table>
  <div class="table-foot"><span>Showing 20-30 of 50 items</span><div class="pager"><span>«</span><span>1</span><span class="on">2</span><span>3</span><span>4</span><span>5</span><span>»</span></div></div>
</section>

<section class="panel" style="left:144px;top:590px;width:282px;height:296px">
  <div class="panel-head">Members<span class="right"><span class="count">35</span></span></div>
  <div class="list">
    <div class="member"><span class="avatar on" role="img" aria-label="Member photo"></span><div><div class="nm">Amelia Nelson</div><div class="role">Admin</div></div></div>
    <div class="member"><span class="avatar on" role="img" aria-label="Member photo"></span><div><div class="nm">Alyssa Molligan</div><div class="role">director</div></div></div>
    <div class="member"><span class="avatar" role="img" aria-label="Member photo"></span><div><div class="nm">Kaitlyn Eddington</div><div class="role">Writer, Mag Editor</div></div></div>
    <div class="member"><span class="avatar on" role="img" aria-label="Member photo"></span><div><div class="nm">Aaron Page</div><div class="role">Blogger</div></div></div>
    <div class="member"><span class="avatar" role="img" aria-label="Member photo"></span><div><div class="nm">Erin Macey</div><div class="role">Writer,</div></div></div>
  </div>
</section>

<section class="panel" style="left:449px;top:590px;width:281px;height:296px">
  <div class="panel-head">Tasks<span class="right"><svg width="3" height="10" viewBox="0 0 3 10" fill="#666"><circle cx="1.5" cy="1.5" r="1.2"/><circle cx="1.5" cy="5" r="1.2"/><circle cx="1.5" cy="8.5" r="1.2"/></svg></span></div>
  <div class="task">
    <div class="timeline">
      <div style="position:absolute;left:6px;top:18px;height:190px;border-left:1px solid #e5e8ec"></div>
      <span class="t-dot" style="top:17px;background:#5cb85c">+</span>
      <span class="t-dot" style="top:71px;background:#8e6bbd">✓</span>
      <span class="t-dot" style="top:125px;background:#e9573f">×</span>
      <span class="t-dot" style="top:180px;background:#3a9ee0">•</span>
    </div>
    <div class="task-list">
      <div class="task-item"><p>Alexandra Jones <span class="m">added a new project</span> to x module</p><div class="time"><span class="clock"></span>Just now</div></div>
      <div class="task-item"><p>Sierra Dickinson <span class="m">is now following you.</span></p><div class="time"><span class="clock"></span>20 minutes ago</div></div>
      <div class="task-item"><p>Olivia Kelly <span class="m">deleted project</span> Norvale</p><div class="time"><span class="clock"></span>46 minutes ago</div></div>
      <div class="task-item"><p>Allison Faber <span class="m">commented your</span> content</p>
        <div class="faces"><span class="avatar" role="img" aria-label="Commenter photo"></span><span class="avatar" role="img" aria-label="Commenter photo"></span><span class="avatar" role="img" aria-label="Commenter photo"></span><span class="avatar" role="img" aria-label="Commenter photo"></span><span class="avatar" role="img" aria-label="Commenter photo"></span></div>
        <div class="time"><span class="clock"></span>2 hours ago</div></div>
    </div>
  </div>
</section>

<section class="panel" style="left:754px;top:590px;width:281px;height:296px">
  <div class="panel-head">Activity<span class="right"><span class="count blue">16</span></span></div>
  <div class="notice">10 members update their activies.<span>×</span></div>
  <div style="position:relative;margin-top:6px">
    <div style="position:absolute;left:29px;top:20px;height:160px;border-left:1px solid #e5e8ec"></div>
    <div class="act-item"><span class="avatar" role="img" aria-label="Member photo"></span><p>Louis Elliot <span class="m">5 min ago</span><br><span class="m">assign you a task</span> report</p></div>
    <div class="act-item"><span class="avatar" role="img" aria-label="Member photo"></span><p>Terry Moore <span class="m">10 min ago</span><br><span class="m">Follow up to close deal</span></p></div>
    <div class="act-item"><span class="avatar" role="img" aria-label="Member photo"></span><p>Walter Paler <span class="m">1 hour ago</span><br><span class="m">was added to</span> Repo</p></div>
    <div class="act-item"><span class="avatar" role="img" aria-label="Member photo"></span><p>Mogen Polish <span class="m">2 hour ago</span><br><span class="m">was added 5 photos to</span> Admin Dashboard</p></div>
  </div>
</section>

<aside class="aside">
  <div class="tab"></div>
  <h3>My Notes</h3>
  <div class="note-btn">Add New Note</div>
  <div class="todo">
    <h4>Todo List</h4>
    <div class="sub">3 of 5 remaining</div>
    <div class="todo-item"><span class="box on"></span>Add New content</div>
    <div class="todo-item"><span class="box"></span>Creating component page</div>
    <div class="todo-item"><span class="box on"></span>Change Password</div>
    <div class="todo-item"><span class="box on"></span>Create new Module</div>
    <div class="todo-item"><span class="box"></span>Update my account</div>
    <div class="todo-add"><span class="in">Add new todo</span><span class="go">Add</span></div>
  </div>
</aside>

</body>
</html>
```